Business card and stationary for a natural medicine company
Herbal drug by plant biotechnology company
Business card and stationary for a natural medicine company - Pharmacy/Pharmaceuticals
Creative Brief
Professional
Soojin Park
President
5817 Briarwood DR Fort Wayne, IN 46825 USA
president@verdolith.com
www.verdolith.com
Please use the catch phrase "New Drugs from Herbal Medicines"
Please print following verse. And by the river upon the bank thereof, on this side and on that side, shall grow all trees for meat, whose leaf shall not fade, neither shall the fruit thereof be consumed: it shall bring forth new fruit according to his months, because their waters they issued out of the sanctuary: and the fruit thereof shall be for meat, and the leaf thereof for medicine. Ezekiel 47:12

```html
<!DOCTYPE html>
<html lang="en">
<head>
<meta charset="utf-8">
<title>Verdolith Business Card</title>
<link href="https://fonts.googleapis.com/css2?family=Open+Sans:wght@400;600&display=swap" rel="stylesheet">
<style>
  :root {
    --backdrop: #d9dadb;
    --navy: #131a45;
    --card-white: #ffffff;
    --teal: #2aa3cf;
    --leaf-green: #8cc63f;
    --ink-grey: #6d6e71;
    --soft-white: #e9ebf5;
  }
  * { margin: 0; padding: 0; box-sizing: border-box; }
  html, body {
    width: 1200px; height: 902px; overflow: hidden;
    background: var(--backdrop);
    font-family: "Open Sans", Arial, sans-serif;
  }
  .canvas { position: relative; width: 1200px; height: 902px; }

  .card {
    position: absolute;
    width: 680px; height: 390px;
    box-shadow: 0 10px 28px rgba(0,0,0,0.18);
    overflow: hidden;
  }

  /* back side */
  .card-back {
    left: 440px; top: 60px;
    background: var(--navy);
    display: flex; align-items: center; justify-content: center;
  }
  .card-back .web {
    color: var(--soft-white);
    font-size: 22px; letter-spacing: 3px;
  }
  .web strong { font-weight: 600; }

  /* front side */
  .card-front {
    left: 120px; top: 460px;
    background: var(--card-white);
  }
  .brand {
    position: absolute; left: 52px; top: 120px;
    display: flex; align-items: center; gap: 14px;
  }
  .brand-mark {
    width: 56px; height: 56px; border-radius: 8px;
    background: var(--teal);
  }
  .brand-name {
    font-size: 42px; font-weight: 400; color: var(--teal);
    letter-spacing: 0.5px;
  }
  .person {
    position: absolute; right: 48px; top: 96px;
    text-align: right;
  }
  .person-name { font-size: 24px; color: var(--teal); font-weight: 400; }
  .person-role { font-size: 20px; color: var(--ink-grey); }

  .contacts {
    position: absolute; left: 52px; top: 232px;
    list-style: none; font-size: 13px; color: var(--ink-grey);
  }
  .contacts li { display: flex; align-items: center; gap: 8px; line-height: 22px; }
  .contacts svg { width: 12px; height: 12px; fill: var(--teal); flex: none; }

  .footer-band { position: absolute; left: 0; bottom: 0; width: 680px; height: 78px; }
  .footer-band .web {
    position: absolute; left: 0; right: 0; bottom: 20px;
    text-align: center; color: var(--soft-white);
    font-size: 18px; letter-spacing: 3px;
  }
</style>
</head>
<body>
<main class="canvas">

  <section class="card card-back" aria-label="Card back">
    <p class="web">www.<strong>verdolith</strong>.com</p>
  </section>

  <section class="card card-front" aria-label="Card front">
    <div class="brand">
      <span class="brand-mark"></span>
      <span class="brand-name">verdolith</span>
    </div>

    <div class="person">
      <p class="person-name">Soojin Park</p>
      <p class="person-role">Owner</p>
    </div>

    <ul class="contacts">
      <li>
        <svg viewBox="0 0 12 12"><path d="M2.5 0.5l2 2.5-1.2 1.2a7 7 0 0 0 4.5 4.5L9 7.5l2.5 2-1.3 2C5 11.5 0.5 7 0.5 1.8z"/></svg>
        555.010.4827
      </li>
      <li>
        <svg viewBox="0 0 12 12"><rect x="0" y="2" width="12" height="8" rx="1"/></svg>
        president@verdolith.com
      </li>
      <li>
        <svg viewBox="0 0 12 12"><path d="M6 0a4 4 0 0 1 4 4c0 3-4 8-4 8S2 7 2 4a4 4 0 0 1 4-4z"/></svg>
        5817 Briarwood DR Fort Wayne, IN 46825 USA
      </li>
    </ul>

    <div class="footer-band">
      <svg width="680" height="78" viewBox="0 0 680 78" aria-hidden="true">
        <polygon points="180,0 680,0 680,6 186,6" fill="var(--leaf-green)"/>
        <polygon points="186,10 680,10 680,78 0,78 0,60" fill="var(--navy)"/>
      </svg>
      <p class="web">www.<strong>verdolith</strong>.com</p>
    </div>
  </section>

</main>
</body>
</html>
```